Website for an interior designer

We need a new website for Clara Beth Holloway whose new business name is Clara Beth Holloway Interiors. She is a residential interior designer with a mix of modern and contemporary tastes. We are in the process of overhauling her website which is +15 years old and not an accurate reflection of her tastes. The uploaded photos are from some of the houses she has done as well as her logo(s). We would need a section for "About Us" that would have a paragraph of text and bullets showing services and a gallery for photos (~12 total, more to come). A contract page would be optional. The client likes the feel/look of this website: https://www.pondrickstudio.example/ but doesn't want to copy it exactly.

Target Market(s)

Upscale home owners

Industry/Entity Type

Interior Design

Coding

Coded - Design and coding required

Number of Pages Required

4 page

Colors

Designer to choose only greyscale colors for use in the design.

Requirements
Must have
• Home page, about us page, gallery page, contact us page.

```html
<!DOCTYPE html>
<html lang="en">
<head>
<meta charset="utf-8">
<title>Clara Beth Holloway Interiors</title>
<link rel="stylesheet" href="https://fonts.googleapis.com/css2?family=Cinzel:wght@400&family=Open+Sans:wght@400;600&display=swap">
<style>
  :root {
    --ink: #3a3a3c;
    --text: #6b6b70;
    --muted: #9a9a9f;
    --heading: #8e8f95;
    --line: #b9b9bd;
    --panel: rgba(168, 162, 166, 0.92);
    --footer: #86878f;
    --white: #ffffff;
  }
  * { box-sizing: border-box; margin: 0; padding: 0; }
  html, body { width: 1200px; height: 2994px; overflow: hidden; background: var(--white); }
  body { position: relative; font-family: "Open Sans", Arial, sans-serif; color: var(--text); }
  .abs { position: absolute; }
  .serif { font-family: "Cinzel", Georgia, serif; font-weight: 400; }

  /* header */
  .contact-line { left: 108px; font-size: 16px; color: var(--text); display: flex; align-items: center; gap: 8px; }
  .contact-line svg { fill: var(--muted); }
  .brand { left: 0; width: 1200px; top: 96px; text-align: center; color: var(--ink); line-height: 1.25; }
  .brand .name { font-size: 28px; letter-spacing: 2px; }
  .brand .sub { font-size: 14px; letter-spacing: 8px; margin-top: 6px; }
  .search { left: 1004px; top: 100px; font-size: 16px; display: flex; align-items: center; gap: 12px; }
  .search svg { stroke: var(--muted); fill: none; }
  .nav { top: 192px; left: 0; width: 1200px; display: flex; justify-content: center; gap: 46px; font-size: 17.5px; color: var(--ink); }
  .nav a { text-decoration: none; color: inherit; display: flex; align-items: center; gap: 18px; }
  .nav a::before { content: ""; width: 10px; height: 10px; background: var(--ink); transform: rotate(45deg); }
  .nav a.active { color: var(--muted); }
  .nav a.active::before { background: var(--line); }

  /* hero */
  .hero-photo { top: 243px; height: 480px; width: 317px; }
  .ph-stair { background: linear-gradient(160deg, #f6f6f4 0%, #dcdcd8 55%, #6a5a4a 100%); }
  .ph-kitchen { background: linear-gradient(180deg, #d9d8d2 0%, #efeeea 50%, #3c3a38 100%); }
  .ph-living { background: linear-gradient(170deg, #5d6670 0%, #8f969b 50%, #b9bbbc 100%); }

  /* about */
  .about-mark { left: 112px; top: 860px; width: 430px; height: 318px; display: flex; align-items: center; justify-content: center; text-align: center; font-size: 52px; line-height: 1.15; color: #c4c5c9; }
  .eyebrow { font-size: 26px; color: var(--heading); letter-spacing: 0.5px; }
  .title { font-size: 42px; color: var(--heading); line-height: 1.25; }
  .about-text { left: 587px; top: 786px; width: 520px; display: flex; flex-direction: column; align-items: flex-start; }
  .about-text .title { font-size: 38px; margin-top: 6px; }
  .about-copy { margin-top: 22px; width: 505px; font-size: 15.5px; line-height: 32.6px; color: var(--text); }
  .about-text .btn { margin-top: 30px; }
  .btn { display: flex; align-items: center; justify-content: center; border: 2px solid var(--line); font-weight: 600; font-size: 17px; letter-spacing: 0.5px; color: var(--muted); }

  /* services */
  .services-photo { left: 112px; top: 1315px; width: 977px; height: 520px; background: linear-gradient(120deg, #e6e4e2 0%, #f3f3f1 45%, #c9cbcc 75%, #eeeeec 100%); }
  .services-panel { left: 112px; top: 1315px; width: 420px; height: 520px; background: var(--panel); color: var(--white); }
  .services-panel .eyebrow, .services-panel .title { color: var(--white); }
  .service-list { list-style: none; position: absolute; left: 40px; top: 135px; width: 360px; font-size: 14.8px; line-height: 19px; }
  .service-list li { position: absolute; left: 0; padding-left: 30px; }
  .btn-light { border-color: var(--white); color: var(--white); }

  /* gallery */
  .gallery-head { left: 0; width: 1200px; text-align: center; }
  .tile { width: 237px; height: 215px; }
  .g1 { background: linear-gradient(160deg, #f4f4f2, #cfcfcc 70%, #6e6458); }
  .g2 { background: linear-gradient(170deg, #4f5861, #8a8f93 60%, #a7a9aa); }
  .g3 { background: linear-gradient(120deg, #e8c24a 0%, #c2553a 55%, #d34f8d 100%); }
  .g4 { background: linear-gradient(180deg, #c8c4a8 0%, #ecebe8 50%, #d8d8d6 100%); }
  .g5 { background: linear-gradient(180deg, #e6e6e6 0%, #6b4a3c 60%, #4a6a3a 100%); }
  .g6 { background: linear-gradient(160deg, #dcdcdc, #f2f2f0 55%, #b8babc); }
  .g7 { background: linear-gradient(180deg, #f1f0ec 0%, #dedad2 60%, #7a5e48 100%); }
  .g8 { background: linear-gradient(140deg, #e2e0dc 0%, #efe9e3 55%, #2e2e30 100%); }

  /* footer */
  .footer { left: 0; top: 2721px; width: 1200px; height: 273px; background: var(--footer); color: var(--white); }
  .footer-mark { left: 537px; top: 2656px; width: 126px; height: 126px; }
  .footer-mark .diamond { position: absolute; left: 18px; top: 18px; width: 90px; height: 90px; background: var(--white); border: 3px solid #9a9ba1; transform: rotate(45deg); }
  .footer-mark .label { position: absolute; inset: 0; display: flex; align-items: center; justify-content: center; text-align: center; font-size: 11px; line-height: 1.3; color: var(--ink); }
  .footer-row { left: 0; width: 1200px; text-align: center; font-size: 16px; color: var(--white); }
  .footer-row .sep { margin: 0 18px; }
  .social { left: 553px; top: 2931px; display: flex; gap: 10px; }
  .social span { width: 25px; height: 25px; background: var(--white); border-radius: 4px; }
</style>
</head>
<body>

<header>
  <div class="abs contact-line" style="top:62px">
    <svg width="14" height="14" viewBox="0 0 24 24"><path d="M6.6 10.8a15 15 0 0 0 6.6 6.6l2.2-2.2c.3-.3.7-.4 1-.2 1.1.4 2.3.6 3.6.6.6 0 1 .4 1 1V20c0 .6-.4 1-1 1C10.6 21 3 13.4 3 4c0-.6.4-1 1-1h3.5c.6 0 1 .4 1 1 0 1.3.2 2.5.6 3.6.1.3 0 .7-.2 1z"/></svg>
    555-014-2290
  </div>
  <div class="abs contact-line" style="top:94px">
    <svg width="16" height="13" viewBox="0 0 24 18"><path d="M0 0h24v2L12 10 0 2z M0 5l12 8 12-8v13H0z"/></svg>
    studio@cbhinteriors.example
  </div>

  <div class="abs brand serif">
    <div class="name">CLARA BETH HOLLOWAY</div>
    <div class="sub">INTERIORS</div>
  </div>

  <div class="abs search">
    <svg width="17" height="17" viewBox="0 0 20 20" stroke-width="2.4"><circle cx="8" cy="8" r="6"/><path d="M12.5 12.5L18 18"/></svg>
    Search
  </div>

  <nav class="abs nav">
    <a class="active" href="#">HOME</a>
    <a href="#">ABOUT US</a>
    <a href="#">GALLERY</a>
    <a href="#">CONTACT US</a>
  </nav>
</header>

<main>
  <div class="abs hero-photo ph-stair" style="left:112px" role="img" aria-label="Bright white entry hall with a curved staircase and tall steel windows"></div>
  <div class="abs hero-photo ph-kitchen" style="left:442px" role="img" aria-label="White dining table and chairs under a brass pendant in an open kitchen"></div>
  <div class="abs hero-photo ph-living" style="left:770px" role="img" aria-label="Grey-panelled family room with bookshelves, fireplace and glass coffee table"></div>

  <section class="about">
    <div class="abs about-mark serif">Clara Beth<br>Holloway</div>
    <div class="abs about-text">
      <div class="eyebrow serif">ABOUT US</div>
      <h1 class="title serif">WELCOME TO CLARA BETH HOLLOWAY INTERIORS</h1>
      <p class="about-copy">Clara Beth Holloway has extensive experience in all aspects of interior design. She has worked on a wide array of residential and commercial projects in her hometown of Houston and across the United States. Clara Beth’s taste can best be described as a sophisticated blend of modern and traditional styles that combine to create a clean, timeless space.</p>
      <a class="btn" style="width:189px;height:58px;text-decoration:none" href="#">ABOUT US</a>
    </div>
  </section>

  <section class="services">
    <div class="abs services-photo" role="img" aria-label="White kitchen with marble island, steel refrigerator and a bowl of green apples"></div>
    <div class="abs services-panel">
      <div class="abs eyebrow serif" style="left:34px;top:22px">SERVICES</div>
      <h2 class="abs title serif" style="left:34px;top:58px">WHAT WE DO</h2>
      <ul class="service-list">
        <li style="top:0">Concept Origination and Project Management</li>
        <li style="top:37px">Review of Proposed Plans for New Construction and Remodels</li>
        <li style="top:94px">Procurement of Furniture, Accents, Art, Fixtures and Fittings</li>
        <li style="top:151px">Selection of Paints, Finishes and Construction Materials</li>
        <li style="top:208px">Vendor Coordination and Recommendations</li>
        <li style="top:245px">Home Staging, Styling and Editing</li>
      </ul>
      <a class="abs btn btn-light" style="left:40px;top:432px;width:171px;height:58px;text-decoration:none" href="#">READ MORE</a>
    </div>
  </section>
  <svg class="abs" style="left:0;top:0;width:0;height:0">
    <defs><symbol id="tick" viewBox="0 0 14 14"><circle cx="7" cy="7" r="7" fill="#fff"/><path d="M3.8 7.2l2.2 2.2 4.2-4.4" fill="none" stroke="#a8a2a6" stroke-width="1.8"/></symbol></defs>
  </svg>
  <svg class="abs" style="left:152px;top:1453px" width="14" height="14"><use href="#tick"/></svg>
  <svg class="abs" style="left:152px;top:1490px" width="14" height="14"><use href="#tick"/></svg>
  <svg class="abs" style="left:152px;top:1547px" width="14" height="14"><use href="#tick"/></svg>
  <svg class="abs" style="left:152px;top:1604px" width="14" height="14"><use href="#tick"/></svg>
  <svg class="abs" style="left:152px;top:1661px" width="14" height="14"><use href="#tick"/></svg>
  <svg class="abs" style="left:152px;top:1698px" width="14" height="14"><use href="#tick"/></svg>

  <section class="gallery">
    <div class="abs gallery-head eyebrow serif" style="top:1908px">GALLERY</div>
    <h2 class="abs gallery-head title serif" style="top:1944px">OUR PROJECTS</h2>

    <div class="abs tile g1" style="left:112px;top:2047px" role="img" aria-label="White spiral staircase in a sunlit hall"></div>
    <div class="abs tile g2" style="left:358px;top:2047px" role="img" aria-label="Grey library room with bookshelves and armchairs"></div>
    <div class="abs tile g3" style="left:605px;top:2047px" role="img" aria-label="Staircase with a vivid multicoloured runner beside yellow artwork"></div>
    <div class="abs tile g4" style="left:851px;top:2047px" role="img" aria-label="White dining area beneath a brass pendant"></div>
    <div class="abs tile g5" style="left:112px;top:2271px" role="img" aria-label="Covered outdoor patio with wicker seating and lawn"></div>
    <div class="abs tile g6" style="left:358px;top:2271px" role="img" aria-label="White kitchen with steel range hood and marble counters"></div>
    <div class="abs tile g7" style="left:605px;top:2271px" role="img" aria-label="Cream living room with beamed ceiling and black-framed windows"></div>
    <div class="abs tile g8" style="left:851px;top:2271px" role="img" aria-label="Curved blush sofa under framed botanical art"></div>

    <a class="abs btn" style="left:515px;top:2540px;width:171px;height:58px;text-decoration:none" href="#">VIEW MORE</a>
  </section>
</main>

<footer>
  <div class="abs footer"></div>
  <div class="abs footer-mark">
    <div class="diamond"></div>
    <div class="label serif">Clara Beth<br>Holloway</div>
  </div>
  <div class="abs footer-row" style="top:2808px">Home<span class="sep">|</span>About us<span class="sep">|</span>Gallery<span class="sep">|</span>Contact us</div>
  <div class="abs footer-row" style="top:2851px">Cell: 555-014-2290<span class="sep">|</span>Email: studio@cbhinteriors.example</div>
  <div class="abs footer-row" style="top:2884px">© 2020,&nbsp; Clara Beth Holloway Interiors.</div>
  <div class="abs social" aria-label="Social links"><span></span><span></span><span></span></div>
</footer>

</body>
</html>
```